Clean Plinth Ads Banner Design For A Finance Company

Hi,
We're a UK based finance company and are looking for new banner ads to use on the Plinth Display Network.
We want the end product to stand out by using strong, minimal design - ideally starting from a dark theme, although I'm open to ideas.
The copy should read:
'Fast Bridging Loans From 0.39% PM'
Once we have these designs agreed, we are looking to replicate them for other products, changing only the text on each ad - for example, 'commercial mortgage service you can rely on' or 'development finance service you can rely on'.
The colours used on our website are the following:
Black - #040303
Orange - #f79124
White - #ffffff
Grey - #ffffff
Example ads that I like - https://www.brimcastle.com/wp-content/uploads/2021/07/plinth-display-ads-example-2-final.png.webp
2 - https://quendrahub.com/wp-content/uploads/2020/03/fbdd56ba3bd16c7a8debb13a411de786.jpg

```html
<!DOCTYPE html>
<html lang="en">
<head>
<meta charset="utf-8">
<title>Arkwell Finance – Bridging Loan Display Banners</title>
<link rel="stylesheet" href="https://fonts.googleapis.com/css2?family=Poppins:wght@400;500;600&display=swap">
<style>
  :root {
    --board: #a7abad;
    --black: #040303;
    --orange: #f79124;
    --white: #ffffff;
    --slate: #56658a;
    --slate-deep: #283049;
  }
  * { margin: 0; padding: 0; box-sizing: border-box; }
  html, body { width: 1200px; height: 966px; overflow: hidden; background: var(--board); }
  body { position: relative; font-family: "Poppins", sans-serif; color: var(--white); }

  .banner { position: absolute; background: var(--black); overflow: hidden; }
  .photo {
    position: absolute; right: 0; bottom: 0;
    background: radial-gradient(ellipse at 70% 70%, var(--slate) 0%, var(--slate-deep) 38%, rgba(4,3,3,0) 72%);
  }
  .brand { position: absolute; color: var(--orange); font-weight: 600; line-height: 0.9; letter-spacing: -0.02em; }
  .brand small { display: block; font-size: 0.3em; letter-spacing: 0.02em; margin-top: 0.15em; }
  .headline { position: absolute; font-weight: 400; line-height: 1.2; white-space: nowrap; }
  .cta {
    position: absolute; border: 1.5px solid var(--orange); border-radius: 999px;
    display: flex; align-items: center; justify-content: center;
    font-weight: 500; text-transform: uppercase; white-space: nowrap;
  }
  .centered { text-align: center; }

  /* 1 – small square */
  .b-small { left: 87px; top: 149px; width: 151px; height: 151px; }
  .b-small .photo { width: 75%; height: 100%; }
  .b-small .brand { left: 10px; top: 10px; font-size: 17px; }
  .b-small .headline { left: 10px; top: 61px; font-size: 11px; line-height: 1.25; }
  .b-small .cta { left: 10px; top: 115px; width: 59px; height: 14px; font-size: 5px; border-width: 1px; }

  /* 2 – square */
  .b-square { left: 262px; top: 111px; width: 189px; height: 189px; }
  .b-square .photo { width: 75%; height: 100%; }
  .b-square .brand { left: 15px; top: 15px; font-size: 21px; }
  .b-square .headline { left: 15px; top: 73px; font-size: 14px; line-height: 1.15; }
  .b-square .cta { left: 15px; top: 129px; width: 70px; height: 17px; font-size: 6px; border-width: 1px; }

  /* 3 – medium rectangle */
  .b-medium { left: 478px; top: 89px; width: 254px; height: 211px; }
  .b-medium .photo { width: 70%; height: 100%; }
  .b-medium .brand { left: 13px; top: 13px; font-size: 24px; }
  .b-medium .headline { left: 13px; top: 75px; font-size: 19px; line-height: 1.2; }
  .b-medium .cta { left: 13px; top: 156px; width: 83px; height: 21px; font-size: 7.5px; }

  /* 4 – leaderboard */
  .b-leader { left: 87px; top: 326px; width: 550px; height: 68px; }
  .b-leader .photo { width: 45%; height: 100%; }
  .b-leader .brand { left: 19px; top: 18px; font-size: 24px; }
  .b-leader .headline { left: 287px; top: 11px; font-size: 14.5px; transform: translateX(-50%); }
  .b-leader .cta { left: 245px; top: 35px; width: 76px; height: 19px; font-size: 7px; }

  /* 5 – slim banner */
  .b-slim { left: 656px; top: 326px; width: 367px; height: 45px; }
  .b-slim .photo { width: 45%; height: 100%; }
  .b-slim .brand { left: 11px; top: 11px; font-size: 19px; }
  .b-slim .headline { left: 189px; top: 6px; font-size: 10.5px; transform: translateX(-50%); }
  .b-slim .cta { left: 158px; top: 23px; width: 57px; height: 14px; font-size: 5px; border-width: 1px; }

  /* 6 – large rectangle */
  .b-large { left: 87px; top: 420px; width: 438px; height: 302px; }
  .b-large .photo { width: 60%; height: 100%; }
  .b-large .brand { left: 25px; top: 23px; font-size: 34px; }
  .b-large .headline { left: 25px; top: 108px; font-size: 28px; line-height: 1.14; }
  .b-large .cta { left: 25px; top: 221px; width: 113px; height: 27px; font-size: 10.5px; }

  /* 7 – skyscraper */
  .b-sky { left: 551px; top: 420px; width: 91px; height: 453px; }
  .b-sky .photo { width: 100%; height: 55%; }
  .b-sky .brand { left: 0; width: 100%; top: 20px; font-size: 24px; text-align: center; }
  .b-sky .headline { left: 0; width: 100%; top: 100px; font-size: 16px; line-height: 1.27; text-align: center; }
  .b-sky .cta { left: 11px; top: 222px; width: 69px; height: 17px; font-size: 6px; border-width: 1px; }

  /* 8 – half page narrow */
  .b-half { left: 670px; top: 420px; width: 181px; height: 302px; }
  .b-half .photo { width: 100%; height: 65%; }
  .b-half .brand { left: 14px; top: 16px; font-size: 22px; }
  .b-half .headline { left: 14px; top: 71px; font-size: 18.5px; line-height: 1.3; }
  .b-half .cta { left: 14px; top: 151px; width: 86px; height: 21px; font-size: 8px; }

  /* 9 – half page */
  .b-tall { left: 877px; top: 420px; width: 227px; height: 453px; }
  .b-tall .photo { width: 100%; height: 68%; }
  .b-tall .brand { left: 17px; top: 18px; font-size: 26px; }
  .b-tall .headline { left: 17px; top: 92px; font-size: 22px; line-height: 1.2; }
  .b-tall .cta { left: 17px; top: 189px; width: 93px; height: 23px; font-size: 8.5px; }
</style>
</head>
<body>

<section class="banner b-small">
  <div class="photo" role="img" aria-label="Calculator, house keyring with keys and a pen on a slate blue desk"></div>
  <div class="brand">arkwell<small>finance</small></div>
  <h2 class="headline">Fast<br>Bridging Loans<br>From 0.39% PM</h2>
  <span class="cta">Learn more</span>
</section>

<section class="banner b-square">
  <div class="photo" role="img" aria-label="Calculator, house keyring with keys and a pen on a slate blue desk"></div>
  <div class="brand">arkwell<small>finance</small></div>
  <h2 class="headline">Fast<br>Bridging Loans<br>From 0.39% PM</h2>
  <span class="cta">Learn more</span>
</section>

<section class="banner b-medium">
  <div class="photo" role="img" aria-label="Calculator, house keyring with keys and a pen on a slate blue desk"></div>
  <div class="brand">arkwell<small>finance</small></div>
  <h2 class="headline">Fast<br>Bridging Loans<br>From 0.39% PM</h2>
  <span class="cta">Learn more</span>
</section>

<section class="banner b-leader">
  <div class="photo" role="img" aria-label="Calculator, house keyring with keys and a pen on a slate blue desk"></div>
  <div class="brand">arkwell<small>finance</small></div>
  <h2 class="headline">Fast Bridging Loans From 0.39% PM</h2>
  <span class="cta">Learn more</span>
</section>

<section class="banner b-slim">
  <div class="photo" role="img" aria-label="Calculator, house keyring with keys and a pen on a slate blue desk"></div>
  <div class="brand">arkwell<small>finance</small></div>
  <h2 class="headline">Fast Bridging Loans From 0.39% PM</h2>
  <span class="cta">Learn more</span>
</section>

<section class="banner b-large">
  <div class="photo" role="img" aria-label="Calculator, house keyring with keys and a pen on a slate blue desk"></div>
  <div class="brand">arkwell<small>finance</small></div>
  <h2 class="headline">Fast<br>Bridging Loans<br>From 0.39% PM</h2>
  <span class="cta">Learn more</span>
</section>

<section class="banner b-sky">
  <div class="photo" role="img" aria-label="Calculator, house keyring with keys and a pen on a slate blue desk"></div>
  <div class="brand">arkwell<small>finance</small></div>
  <h2 class="headline">Fast<br>Bridging<br>Loans<br>From<br>0.39% PM</h2>
  <span class="cta">Learn more</span>
</section>

<section class="banner b-half">
  <div class="photo" role="img" aria-label="Calculator, house keyring with keys and a pen on a slate blue desk"></div>
  <div class="brand">arkwell<small>finance</small></div>
  <h2 class="headline">Fast<br>Bridging Loans<br>From 0.39% PM</h2>
  <span class="cta">Learn more</span>
</section>

<section class="banner b-tall">
  <div class="photo" role="img" aria-label="Calculator, house keyring with keys and a pen on a slate blue desk"></div>
  <div class="brand">arkwell<small>finance</small></div>
  <h2 class="headline">Fast<br>Bridging Loans<br>From 0.39% PM</h2>
  <span class="cta">Learn more</span>
</section>

</body>
</html>
```